ALL TEXT Social Media Graphics

We are looking for a series of social media graphics for Instagram (new size: 4:5 (1080 x 1350 pixels) ratio that are ALL TEXT. We want the following quotes below on each graphic; one quote per graphic. AND, In very small letters at the bottom of each graphic, add @PaulaWrenLive
The look and feel of these graphics should be complimentary to the color palette attached below; but keep them simple. But the design is up to you; at the end of this document, I provided various samples of all text graphics that I like as examples.
The Quotes are in the attached WORD document
women trying to lose weight

```html
<!DOCTYPE html>
<html lang="en">
<head>
<meta charset="utf-8">
<title>Summer Shapeup – All Text Social Graphics</title>
<link rel="stylesheet" href="https://fonts.googleapis.com/css2?family=Roboto:wght@300;400&display=swap">
<style>
  :root {
    --page: #ffffff;
    --berry: #ae1d57;
    --rose: #f06292;
    --blush: #f291b3;
    --petal: #f7bfd7;
    --ink: #ffffff;
  }
  html, body {
    margin: 0;
    padding: 0;
    width: 849px;
    height: 1200px;
    overflow: hidden;
    background: var(--page);
  }
  .sheet {
    position: relative;
    width: 849px;
    height: 1200px;
  }
  .post {
    position: absolute;
    width: 119px;
    height: 149px;
    overflow: hidden;
  }
  .post__bg {
    position: absolute;
    inset: 0;
  }
  .bg-rose-berry  { background: linear-gradient(160deg, var(--berry) 0%, var(--rose) 45%, var(--rose) 75%, var(--blush) 100%); }
  .bg-blush-petal { background: linear-gradient(110deg, var(--rose) 0%, var(--blush) 35%, var(--blush) 70%, var(--petal) 100%); }
  .bg-rose-mix    { background: linear-gradient(135deg, var(--berry) 0%, var(--rose) 40%, var(--blush) 100%); }
  .bg-blush-soft  { background: linear-gradient(160deg, var(--rose) 0%, var(--blush) 35%, var(--blush) 70%, var(--petal) 100%); }
  .bg-rose-deep   { background: linear-gradient(20deg, var(--berry) 0%, var(--rose) 45%, var(--rose) 80%, var(--blush) 100%); }
  .bg-berry-rose  { background: linear-gradient(200deg, var(--rose) 0%, var(--berry) 55%, var(--berry) 100%); }
  .bg-berry-top   { background: linear-gradient(180deg, var(--berry) 0%, var(--berry) 30%, var(--rose) 80%, var(--rose) 100%); }
  .bg-rose-blush  { background: linear-gradient(90deg, var(--berry) 0%, var(--rose) 25%, var(--rose) 70%, var(--blush) 100%); }
  .bg-rose-right  { background: linear-gradient(250deg, var(--berry) 0%, var(--rose) 40%, var(--rose) 70%, var(--blush) 100%); }
  .bg-blush-rose  { background: linear-gradient(100deg, var(--blush) 0%, var(--blush) 35%, var(--rose) 70%, var(--berry) 100%); }
  .post__quote {
    position: absolute;
    left: 19px;
    right: 2px;
    margin: 0;
    font-family: "Roboto", sans-serif;
    font-weight: 300;
    font-size: 8.2px;
    line-height: 10.1px;
    letter-spacing: 0;
    color: var(--ink);
    white-space: nowrap;
  }
  .post__quote--top { top: 23px; }
  .post__quote--mid { top: 33px; }
  .post__quote--low { top: 37px; }
  .post__handle {
    position: absolute;
    left: 19px;
    top: 120px;
    margin: 0;
    font-family: "Roboto", sans-serif;
    font-weight: 300;
    font-size: 4.9px;
    color: var(--ink);
    opacity: 0.85;
  }
  .post__handle--faint { opacity: 0.6; }
  .row-1 { top: 445px; }
  .row-2 { top: 605px; }
  .col-1 { left: 104px; }
  .col-2 { left: 234px; }
  .col-3 { left: 365px; }
  .col-4 { left: 495px; }
  .col-5 { left: 625px; }
</style>
</head>
<body>
<main class="sheet">

  <article class="post row-1 col-1">
    <div class="post__bg bg-rose-berry" role="img" aria-label="Layered pink wave pattern background"></div>
    <p class="post__quote post__quote--top">You can absolutely be<br>down 20–30 pounds<br>by end of summer. All<br>it takes is the right<br>plan—and you’ve<br>found it.<br>Comment “Hot Girl”<br>for the Hot Girl<br>Summer Shapeup!</p>
    <p class="post__handle">@PaulaWrenLive</p>
  </article>

  <article class="post row-1 col-2">
    <div class="post__bg bg-blush-petal" role="img" aria-label="Layered pink wave pattern background"></div>
    <p class="post__quote post__quote--top">You don’t need<br>another diet—you<br>need a system that<br>works. Drop 30<br>pounds with the Hot<br>Girl Summer<br>Shapeup.<br>Comment “Summer”<br>to start now.</p>
    <p class="post__handle post__handle--faint">@PaulaWrenLive</p>
  </article>

  <article class="post row-1 col-3">
    <div class="post__bg bg-rose-mix" role="img" aria-label="Layered pink wave pattern background"></div>
    <p class="post__quote post__quote--top">This summer ain’t<br>over—and neither are<br>your body goals. Drop<br>30 pounds with the<br>Hot Girl Summer<br>Shapeup.<br>Comment “Hot Girl” to<br>get the plan</p>
    <p class="post__handle">@PaulaWrenLive</p>
  </article>

  <article class="post row-1 col-4">
    <div class="post__bg bg-blush-soft" role="img" aria-label="Layered pink wave pattern background"></div>
    <p class="post__quote post__quote--mid">If your goal is a tiny<br>waist, flat belly, and<br>30 pounds down—this<br>is the plan.<br>Comment “Summer”<br>to join the Hot Girl<br>Summer Shapeup!</p>
    <p class="post__handle post__handle--faint">@PaulaWrenLive</p>
  </article>

  <article class="post row-1 col-5">
    <div class="post__bg bg-rose-deep" role="img" aria-label="Layered pink wave pattern background"></div>
    <p class="post__quote post__quote--mid">There’s still time to<br>drop the 30 pounds<br>and slay this summer.<br>The Hot Girl Summer<br>Shapeup has the<br>blueprint.<br>Comment “Hot Girl”!</p>
    <p class="post__handle">@PaulaWrenLive</p>
  </article>

  <article class="post row-2 col-1">
    <div class="post__bg bg-berry-rose" role="img" aria-label="Layered pink wave pattern background"></div>
    <p class="post__quote post__quote--top">Snatched waist, flat<br>tummy, 30 pounds<br>lighter —that’s what<br>the Hot Girl Summer<br>Shapeup Challenge<br>delivers.<br>Comment “Hot Girl”<br>to get the plan</p>
    <p class="post__handle">@PaulaWrenLive</p>
  </article>

  <article class="post row-2 col-2">
    <div class="post__bg bg-berry-top" role="img" aria-label="Layered pink wave pattern background"></div>
    <p class="post__quote post__quote--top">Nothing feels better<br>than seeing that scale<br>drop week after week.<br>Let’s lose up to 30<br>pounds this<br>summer—together.<br>Comment “Summer”<br>to join the Hot Girl<br>Summer Shapeup!</p>
    <p class="post__handle">@PaulaWrenLive</p>
  </article>

  <article class="post row-2 col-3">
    <div class="post__bg bg-rose-blush" role="img" aria-label="Layered pink wave pattern background"></div>
    <p class="post__quote post__quote--low">Sis, we’re dropping<br>belly flat and saying<br>goodbye to stubborn<br>pounds. Join the Hot<br>Girl Summer Shapeup<br>comment “Summer”!</p>
    <p class="post__handle">@PaulaWrenLive</p>
  </article>

  <article class="post row-2 col-4">
    <div class="post__bg bg-rose-right" role="img" aria-label="Layered pink wave pattern background"></div>
    <p class="post__quote post__quote--low">Don’t wait ‘til next<br>summer to get right.<br>The time is NOW.<br>Drop 30 pounds with<br>the Hot Girl Summer<br>Shapeup.<br>Comment “Summer”!</p>
    <p class="post__handle post__handle--faint">@PaulaWrenLive</p>
  </article>

  <article class="post row-2 col-5">
    <div class="post__bg bg-blush-rose" role="img" aria-label="Layered pink wave pattern background"></div>
    <p class="post__quote post__quote--top">You’ve got 8 weeks<br>and the perfect plan<br>to drop 30 pounds.<br>Let’s get snatched this<br>summer with the Hot<br>Girl Summer<br>Shapeup.<br>Comment “Summer”!</p>
    <p class="post__handle post__handle--faint">@PaulaWrenLive</p>
  </article>

</main>
</body>
</html>
```